Brochure design for HVAC Company

A classic tri-fold brochure design for an air conditioning, refrigeration, and heating company. Would like the designs to be simple (uncluttered), professional, and pull in the logo colors. Attached is the logo and a business card designs. The company name is Bluestem Valley Air Conditioning, Refrigeration, and Heating.

Target Market(s)

Businesses normally food establishments for refrigeration and ice machines. Looking to sell them on maintenance plan: Gold, Silver, and Bronze. The material should help them to understand the services offered: Maintenance, Servicing and Troubleshooting, and Installations of ice machines, commercial refrigeration, and walk-in freezers and air conditioning (duct, ductless, and rooftop)

Industry/Entity Type

Hvac

Font styles to use
Sans Serif

Requirements
Must have
• Include standard information, such as company name, at least two types of contact information (phone, email and post office address), a logo and tagline. It should also include a headline on the front and two or three brief items outlining benefits your organization can provide.
• Tagline is approximately 14 words and 66 characters.
• Looking to inform customers of services offered: maintenance three plans gold, silver, and bronze, servicing and troubleshooting, and installation.
• Products Serviced, maintained, and installed: Commercial refrigeration, Ice Machines, Air Conditioning (both duct, ductless, and rooftop), walk in freezers.
• Call to action is $100 off on signed maintenance contract. $50 off on first service call.
• Use lorem ipsum text to complement the details of the above information. I will add it later before printing.
• Use logo color scheme and any other colors that complement it.
• Would like this to be a word template.
Nice to have
• Can you make this a Microsoft Word template? Sketch is good, or adobe cs4 format.
Should not have
• Photos should NOT be focused on the homeowner. Should BE focused on the commercial side of the business. Photos can be from any of these product areas: commercial refrigeration, ice machine, walk in freezer boxes, and light roof top ac and heating units.

```html
<!DOCTYPE html>
<html lang="en">
<head>
<meta charset="utf-8">
<title>Bluestem Valley Tri-fold Brochure</title>
<link rel="stylesheet" href="https://fonts.googleapis.com/css2?family=Arimo:ital,wght@0,400;0,700;1,400;1,700&display=swap">
<style>
  :root {
    --blue: #4a6ab4;
    --blue-soft: #6683c4;
    --orange: #f2935d;
    --orange-deep: #ec7f45;
    --dark: #262626;
    --paper: #ececec;
    --page-bg: #d9d9d9;
    --white: #ffffff;
  }
  * { margin: 0; padding: 0; box-sizing: border-box; }
  html, body { width: 1200px; height: 1200px; overflow: hidden; }
  body { background: var(--page-bg); font-family: "Arimo", Arial, sans-serif; color: var(--white); position: relative; }

  .spread { position: absolute; left: 50px; width: 1100px; height: 540px; overflow: hidden; background: var(--white); box-shadow: 0 6px 18px rgba(0,0,0,.25); }
  .spread--outside { top: 40px; }
  .spread--inside { top: 620px; }
  .band-top { position: absolute; left: 0; top: 0; width: 100%; height: 28px; background: var(--blue); z-index: 3; }
  .band-bottom { position: absolute; left: 0; bottom: 0; width: 100%; height: 28px; background: var(--dark); z-index: 3; }
  .panel { position: absolute; top: 28px; height: 484px; width: 366.67px; overflow: hidden; }
  .panel--services { left: 0; background: var(--orange); }
  .panel--contact { left: 366.67px; }
  .panel--cover { left: 733.33px; background: var(--paper); }
  .fold { position: absolute; top: 0; width: 1px; height: 100%; background: rgba(0,0,0,.12); z-index: 4; }

  .photo { position: absolute; }
  .photo--fridges { left: 0; bottom: 0; width: 100%; height: 190px; background: linear-gradient(180deg, #e0875a 0%, #8a8f9a 35%, #5c6f86 60%, #b8c2cc 100%); }
  .photo--rooftop { inset: 0; background: linear-gradient(180deg, #dfe7f2 0%, #c9ced6 40%, #8b9099 70%, #b7b3ac 100%); }
  .photo--technician { left: 0; top: 132px; width: 100%; height: 220px; background: linear-gradient(135deg, #e6e8ec 0%, #cfd4da 45%, #3b55a8 75%, #e8ebee 100%); }
  .photo--store { inset: 0; background: linear-gradient(90deg, #b9bdc2 0%, #dcdfe2 35%, #c6d2e0 65%, #8eb0d6 100%); }
  .photo--store::after { content: ""; position: absolute; left: 0; right: 0; bottom: 0; height: 45%; background: linear-gradient(180deg, rgba(90,100,120,0) 0%, rgba(80,95,120,.55) 100%); }

  .services { position: absolute; left: 34px; top: 30px; width: 310px; z-index: 2; }
  .services__title { font-weight: 700; font-style: italic; font-size: 17px; margin-bottom: 10px; }
  .services__title--second { margin-top: 32px; }
  .offer-list { list-style: none; font-size: 14px; line-height: 1.6; }
  .offer-list li { display: flex; align-items: flex-start; gap: 8px; }
  .offer-list .icon { flex: none; width: 15px; height: 15px; margin-top: 4px; }
  .offer-list__sub { font-style: italic; padding-left: 36px; display: block; }
  .services__intro { font-size: 14px; padding-left: 10px; margin-bottom: 4px; }
  .product-list { list-style: none; font-size: 14px; line-height: 1.6; padding-left: 10px; }
  .product-list li::before { content: ""; display: inline-block; width: 10px; height: 10px; border-radius: 50%; background: var(--white); margin-right: 8px; }
  .product-list .note { font-size: 11px; padding-left: 6px; }
  .product-list .note::before { display: none; }

  .contact-card { position: absolute; left: 10px; bottom: 0; width: 256px; height: 232px; background: rgba(242,147,93,.93); padding: 26px 22px 0 40px; }
  .contact-card__name { font-size: 16px; letter-spacing: .5px; }
  .contact-card__role { font-size: 12px; margin-bottom: 30px; }
  .contact-row { display: flex; gap: 10px; align-items: flex-start; font-size: 14px; margin-bottom: 18px; }
  .contact-row--small { font-size: 12.5px; }
  .contact-row svg { flex: none; width: 18px; height: 18px; }

  .brand { position: absolute; left: 0; top: 0; width: 100%; height: 132px; display: flex; align-items: center; justify-content: center; gap: 10px; }
  .brand__dot { width: 22px; height: 22px; border-radius: 50%; background: var(--orange-deep); }
  .brand__name { font-weight: 700; font-size: 21px; color: var(--blue); }
  .cover-info { position: absolute; left: 0; bottom: 0; width: 100%; height: 132px; background: var(--blue-soft); text-align: center; padding: 10px 30px 0; }
  .cover-info__tagline { font-size: 10.5px; line-height: 1.35; }
  .cover-info__web { font-size: 12px; margin-top: 36px; }

  .special { position: absolute; left: 270px; top: 135px; width: 422px; height: 265px; background: rgba(242,147,93,.93); text-align: center; padding-top: 26px; z-index: 2; }
  .special__title { font-style: italic; font-size: 27px; letter-spacing: .5px; }
  .special__lead { font-size: 16px; margin-top: 12px; }
  .special__amount { font-size: 30px; margin-top: 8px; line-height: 1.1; }
  .special__terms { font-size: 16px; }
  .special__rule { width: 270px; margin: 10px auto 8px; border-top: 1px dashed rgba(255,255,255,.75); }
</style>
</head>
<body>

<section class="spread spread--outside" aria-label="Brochure outside">
  <div class="band-top"></div>

  <div class="panel panel--services">
    <div class="photo photo--fridges" role="img" aria-label="Photo of lit commercial refrigerator cases in a store aisle"></div>
    <div class="services">
      <h2 class="services__title">We Offer</h2>
      <ul class="offer-list">
        <li><svg class="icon" viewBox="0 0 16 16"><circle cx="8" cy="8" r="5" fill="none" stroke="#fff" stroke-width="3.2" stroke-dasharray="2.2 1.7"/><circle cx="8" cy="8" r="2.6" fill="#fff"/></svg><span>Maintenance three plans</span></li>
        <li><span class="offer-list__sub">Gold, Silver, Bronze,</span></li>
        <li><svg class="icon" viewBox="0 0 16 16"><circle cx="8" cy="8" r="5" fill="none" stroke="#fff" stroke-width="3.2" stroke-dasharray="2.2 1.7"/><circle cx="8" cy="8" r="2.6" fill="#fff"/></svg><span>Servicing and Troubleshooting,</span></li>
        <li><svg class="icon" viewBox="0 0 16 16"><circle cx="8" cy="8" r="5" fill="none" stroke="#fff" stroke-width="3.2" stroke-dasharray="2.2 1.7"/><circle cx="8" cy="8" r="2.6" fill="#fff"/></svg><span>Installation.</span></li>
      </ul>
      <h2 class="services__title services__title--second">Products Services</h2>
      <p class="services__intro">Maintained, and Installed:</p>
      <ul class="product-list">
        <li>Commercial refrigeration,</li>
        <li>Ice Machines,</li>
        <li>Air conditioning</li>
        <li class="note">(both duct, ductless, and rooftop),</li>
        <li>Walk in freezers</li>
      </ul>
    </div>
  </div>

  <div class="panel panel--contact">
    <div class="photo photo--rooftop" role="img" aria-label="Photo of commercial rooftop condenser units against a blue sky"></div>
    <div class="contact-card">
      <p class="contact-card__name">DANIEL PORTER</p>
      <p class="contact-card__role">Mechanic</p>
      <div class="contact-row">
        <svg viewBox="0 0 24 24"><path fill="#3d5fb0" d="M6.6 10.8a15.1 15.1 0 0 0 6.6 6.6l2.2-2.2a1 1 0 0 1 1-.25 11.4 11.4 0 0 0 3.6.57 1 1 0 0 1 1 1V20a1 1 0 0 1-1 1A17 17 0 0 1 3 4a1 1 0 0 1 1-1h3.5a1 1 0 0 1 1 1c0 1.25.2 2.45.57 3.57a1 1 0 0 1-.25 1z"/></svg>
        <span>555 014 0178</span>
      </div>
      <div class="contact-row contact-row--small">
        <svg viewBox="0 0 24 24"><path fill="#3d5fb0" d="M12 2a7 7 0 0 0-7 7c0 5.2 7 13 7 13s7-7.8 7-13a7 7 0 0 0-7-7zm0 9.5A2.5 2.5 0 1 1 12 6.5a2.5 2.5 0 0 1 0 5z"/></svg>
        <span>PO Box 218, Cedar Falls,<br>NY 11000</span>
      </div>
      <div class="contact-row contact-row--small">
        <svg viewBox="0 0 24 24"><rect x="2" y="5" width="20" height="14" rx="1" fill="#3d5fb0"/><path d="M2.5 6l9.5 7 9.5-7" fill="none" stroke="#f2935d" stroke-width="1.6"/></svg>
        <span>daniel@bluestemhvac.com</span>
      </div>
    </div>
  </div>

  <div class="panel panel--cover">
    <div class="brand">
      <span class="brand__dot"></span>
      <span class="brand__name">BLUESTEM VALLEY</span>
    </div>
    <div class="photo photo--technician" role="img" aria-label="Photo of a technician's gloved hand servicing an air conditioning unit with a screwdriver"></div>
    <div class="cover-info">
      <p class="cover-info__tagline">"Bluestem Valley" is Cedar Falls's most trusted source for air conditioning, refriearation and heating services.</p>
      <p class="cover-info__web">www.bluestemhvac.com</p>
    </div>
  </div>

  <div class="fold" style="left:366.67px"></div>
  <div class="fold" style="left:733.33px"></div>
  <div class="band-bottom"></div>
</section>

<section class="spread spread--inside" aria-label="Brochure inside">
  <div class="band-top"></div>
  <div class="panel" style="left:0;width:1100px">
    <div class="photo photo--store" role="img" aria-label="Panoramic photo of a walk-in cooler, rooftop condenser and stocked refrigerated store shelves"></div>
    <div class="special" style="top:107px">
      <h2 class="special__title">SPECIAL OFFER</h2>
      <p class="special__lead">Call to action is</p>
      <p class="special__amount">$100 off</p>
      <p class="special__terms">on signed maintenance contract.</p>
      <div class="special__rule"></div>
      <p class="special__amount">$50 off</p>
      <p class="special__terms">on first service call.</p>
    </div>
  </div>
  <div class="fold" style="left:366.67px"></div>
  <div class="fold" style="left:733.33px"></div>
  <div class="band-bottom"></div>
</section>

</body>
</html>
```